Billboard design for a small town Oral Surgeon

We are getting several billboards and need a design that highlights the doctors photo, and bullet points of what he does. Our business name is extremely long, so it’s a challenge to figure out how to do this. Maybe just use our logo? Open to ideas.
The logo can be shortened as designer sees fit, meaning we can drop the tag line. Important info to include:
Doctors name is Lorvik Tamsen
The highlighted bullet points are:
•Implants
•wisdom teeth
•Jaw Surgery
•facial trauma
The goal of this billboard is to let our community know that they have an option here in Ada, our town. Many still drive to the city a couple hours away not knowing they now have an option here at home. Having a hard time finding examples of what I have in mind, so hoping this will get us going. I want it as “non-busy” as possible, so no unnecessary lines or anything that competes with the information we are trying to get across.

Target Market(s)

Everyone in town, just trying to spread the word that we are here

Industry/Entity Type

Medical/surgical (oral surgery)

Font styles to use
Sans Serif

Colors
0094D4
00A9DD
6FCCEA
C7EBF8
E9F6FB

Requirements
Must have
• *New note** Due to location of billboard, I prefer the photo of doctor to be on the left side. Must look neat and professional. Must highlight what we do.
Nice to have
• Our colors are a blue-green with silver, against black or white, but I’m flexible on this, I don’t necessarily need the colors highlighted. I’m also flexible on font style, just needs to be easy to read.
Should not have
• Distracting graphics, should not look like a dental office. That’s an issue we have is people thinking we are another dental office, we do not do any general dentistry, it’s surgery only.

```html
<!DOCTYPE html>
<html lang="en">
<head>
<meta charset="utf-8">
<title>Ridgeline Oral &amp; Maxillofacial Surgery – Billboard</title>
<link rel="stylesheet" href="https://fonts.googleapis.com/css2?family=Archivo:wght@500;900&display=swap">
<style>
  :root {
    --teal: #1197aa;
    --teal-deep: #0a8a9d;
    --band: #167880;
    --white: #ffffff;
    --ink: #4a5a63;
    --accent: #2aa6c4;
    --photo-top: #2f8f9c;
    --photo-mid: #c79a84;
    --photo-low: #1d2533;
  }
  * { margin: 0; padding: 0; box-sizing: border-box; }
  html, body { width: 1200px; height: 630px; overflow: hidden; background: var(--white); }
  .billboard {
    position: relative;
    width: 1200px; height: 630px;
    background: linear-gradient(180deg, var(--teal-deep) 0%, var(--teal) 40%);
    overflow: hidden;
    font-family: "Archivo", sans-serif;
  }
  .doctor-photo {
    position: absolute;
    left: 0; top: 56px;
    width: 440px; height: 574px;
    border-radius: 180px 180px 0 0;
    background: linear-gradient(180deg, var(--photo-top) 0%, var(--photo-mid) 35%, var(--photo-mid) 55%, var(--photo-low) 80%);
  }
  .services {
    position: absolute;
    left: 400px; top: 110px;
    list-style: none;
  }
  .services li {
    position: relative;
    padding-left: 44px;
    font-weight: 900;
    font-size: 54px;
    line-height: 92px;
    letter-spacing: 1px;
    color: var(--white);
    text-transform: uppercase;
    white-space: nowrap;
  }
  .services li::before {
    content: "";
    position: absolute;
    left: 0; top: 37px;
    width: 18px; height: 18px;
    border-radius: 50%;
    background: var(--white);
  }
  .name-band {
    position: absolute;
    left: 440px; bottom: 0;
    width: 760px; height: 99px;
    background: var(--band);
    border-top-left-radius: 40px;
    display: flex; align-items: center;
    padding-left: 40px;
  }
  .doctor-name {
    font-weight: 500;
    font-size: 40px;
    letter-spacing: 1px;
    color: var(--white);
    text-transform: uppercase;
  }
  .practice-mark {
    position: absolute;
    left: 1000px; top: 125px;
    width: 158px; height: 142px;
    background: var(--white);
    border-radius: 20px;
    display: flex; flex-direction: column;
    align-items: center; justify-content: center;
    gap: 10px;
    padding: 0 10px;
  }
  .practice-dot {
    width: 40px; height: 40px;
    border-radius: 50%;
    background: var(--accent);
  }
  .practice-name {
    font-weight: 500;
    font-size: 10px;
    line-height: 1.25;
    text-align: center;
    text-transform: uppercase;
    color: var(--ink);
  }
</style>
</head>
<body>
  <main class="billboard">
    <div class="doctor-photo" role="img" aria-label="Portrait photo of Dr. Lorvik Tamsen, smiling, in a dark suit and red tie"></div>

    <ul class="services">
      <li>Implants</li>
      <li>Wisdom Teeth</li>
      <li>Jaw Surgery</li>
      <li>Facial Trauma</li>
    </ul>

    <div class="practice-mark">
      <span class="practice-dot"></span>
      <p class="practice-name">Ridgeline Oral &amp;<br>Maxillofacial Surgery</p>
    </div>

    <div class="name-band">
      <p class="doctor-name">Doctors.Lorvik Tamsen</p>
    </div>
  </main>
</body>
</html>
```